Boutique Soy Candle Company Needs a Label Design

We need a label design for a boutique soy candle company based in Saltmere, South Australia.
We sell high quality, hand poured soy wax candles, melts and reed diffusers.
We are based in a coastal town and would like the label to reflect our rustic, beachy, retro but luxurious feel. I've attached the design we've been using and like the idea but want to have something more professional. The picture of the Tandry Column is something that we would like to be included somehow - it's like our town symbol - a 'lighthouse' of sorts. It was quite stylised on my original design but we are open to different interpretations.
We like the idea of a 'Kraft' brown paper sort of label but are not set on it. We also love the fluro pink look.

```html
<!DOCTYPE html>
<html lang="en">
<head>
<meta charset="utf-8">
<title>Glimmer Soy Candle Co. – Label Set</title>
<link href="https://fonts.googleapis.com/css2?family=Montserrat:wght@800&display=swap" rel="stylesheet">
<style>
  :root {
    --backdrop: #3d3d3d;
    --paper: #ffffff;
    --fluro-pink: #e5097f;
  }
  * { margin: 0; padding: 0; box-sizing: border-box; }
  html, body { width: 1200px; height: 1120px; overflow: hidden; background: var(--backdrop); }
  .canvas { position: relative; width: 1200px; height: 1120px; background: var(--backdrop); font-family: "Montserrat", Arial, sans-serif; color: var(--fluro-pink); }

  .label { position: absolute; width: 424px; height: 455px; background: var(--paper); }
  .label--small { left: 150px; top: 87px; }
  .label--large { left: 626px; top: 87px; }
  .label--panelled { left: 388px; top: 578px; }

  .label__frame { position: absolute; inset: 0; width: 100%; height: 100%; }
  .label__frame .rule { fill: none; stroke: var(--fluro-pink); }
  .label__frame .corner { fill: var(--fluro-pink); }

  .brand { position: absolute; left: 0; right: 0; text-align: center; font-weight: 800; text-transform: uppercase; }
  .brand__dot { display: block; margin: 0 auto; border-radius: 50%; background: var(--fluro-pink); }
  .brand__name { display: block; line-height: 1; letter-spacing: 0.02em; }
  .brand__line { display: block; line-height: 1.05; letter-spacing: 0.04em; }

  .label--small .brand, .label--panelled .brand { top: 38px; }
  .label--small .brand__dot, .label--panelled .brand__dot { width: 66px; height: 66px; margin-bottom: 12px; }
  .label--small .brand__name, .label--panelled .brand__name { font-size: 40px; }
  .label--small .brand__line, .label--panelled .brand__line { font-size: 12px; margin-top: 8px; }

  .label--large .brand { top: 62px; }
  .label--large .brand__dot { width: 92px; height: 92px; margin-bottom: 18px; }
  .label--large .brand__name { font-size: 62px; }
  .label--large .brand__line { font-size: 15px; margin-top: 12px; }

  .provenance { position: absolute; left: 0; right: 0; text-align: center; font-weight: 800; font-size: 10.5px; line-height: 13px; letter-spacing: 0.03em; text-transform: uppercase; }
  .label--small .provenance { top: 345px; }
  .label--large .provenance { top: 322px; }
  .label--panelled .provenance { top: 316px; }

  .flourish { display: block; width: 56px; height: 9px; margin: 0 auto; background: var(--fluro-pink); border-radius: 4px; opacity: 0.85; }
  .flourish--top { margin-bottom: 9px; }
  .flourish--bottom { margin-top: 9px; }
</style>
</head>
<body>
<main class="canvas">

  <section class="label label--small">
    <svg class="label__frame" viewBox="0 0 424 455" aria-hidden="true">
      <rect class="rule" x="14" y="14" width="396" height="427" stroke-width="4"/>
      <rect class="rule" x="26" y="26" width="372" height="403" stroke-width="1.5"/>
      <path class="corner" d="M26 26h18l-18 18z M398 26h-18l18 18z M26 429h18l-18-18z M398 429h-18l18-18z"/>
    </svg>
    <div class="brand">
      <span class="brand__dot"></span>
      <span class="brand__name">Glimmer</span>
      <span class="brand__line">Soy Candle Co.</span>
    </div>
    <div class="provenance">
      <span class="flourish flourish--top" role="img" aria-label="Small decorative flourish"></span>
      <p>Hand poured in Saltmere, South Australia</p>
      <p>All natural soy</p>
      <span class="flourish flourish--bottom" role="img" aria-label="Small decorative flourish"></span>
    </div>
  </section>

  <section class="label label--large">
    <svg class="label__frame" viewBox="0 0 424 455" aria-hidden="true">
      <rect class="rule" x="14" y="14" width="396" height="427" stroke-width="4"/>
      <rect class="rule" x="26" y="26" width="372" height="403" stroke-width="1.5"/>
      <path class="corner" d="M26 26h18l-18 18z M398 26h-18l18 18z M26 429h18l-18-18z M398 429h-18l18-18z"/>
    </svg>
    <div class="brand">
      <span class="brand__dot"></span>
      <span class="brand__name">Glimmer</span>
      <span class="brand__line">Soy Candle Co.</span>
    </div>
    <div class="provenance">
      <span class="flourish flourish--top" role="img" aria-label="Small decorative flourish"></span>
      <p>Hand poured in Saltmere, South Australia</p>
      <p>All natural soy</p>
      <span class="flourish flourish--bottom" role="img" aria-label="Small decorative flourish"></span>
    </div>
  </section>

  <section class="label label--panelled">
    <svg class="label__frame" viewBox="0 0 424 455" aria-hidden="true">
      <rect class="rule" x="14" y="14" width="396" height="427" stroke-width="4"/>
      <rect class="rule" x="26" y="26" width="372" height="359" stroke-width="1.5"/>
      <line class="rule" x1="26" y1="217" x2="398" y2="217" stroke-width="1.5"/>
      <line class="rule" x1="26" y1="305" x2="398" y2="305" stroke-width="1.5"/>
      <line class="rule" x1="14" y1="386" x2="410" y2="386" stroke-width="4"/>
      <line class="rule" x1="244" y1="386" x2="244" y2="441" stroke-width="3"/>
      <path class="corner" d="M26 26h18l-18 18z M398 26h-18l18 18z M26 217h14l-14 12z M398 217h-14l14 12z M26 305h14l-14-12z M398 305h-14l14-12z M26 385h14l-14-12z M398 385h-14l14-12z"/>
    </svg>
    <div class="brand">
      <span class="brand__dot"></span>
      <span class="brand__name">Glimmer</span>
      <span class="brand__line">Soy Candle Co.</span>
    </div>
    <div class="provenance">
      <span class="flourish flourish--top" role="img" aria-label="Small decorative flourish"></span>
      <p>Hand poured in Saltmere, South Australia</p>
      <p>All natural soy</p>
      <span class="flourish flourish--bottom" role="img" aria-label="Small decorative flourish"></span>
    </div>
  </section>

</main>
</body>
</html>
```